Menu and Logo Design for Dine in Indian restaurant

We are an Indian Restaurant(TaalVan) based in Ottawa, Ontario, Canada. We would like a menu designed for our dine-in customers. The interior of the restaurant is contemporary, fine-dine, prices are slightly on the premium side. We offer quality food and generous portions. The menu design should be clear and not too busy. Some menu items shall have descriptions .

Font styles to use
Decorative
Other font styles liked:
• Devnagari font and decorative font with mandala

Colors
59FF00
82FF00
B8FF75
E3FFCB
F4FFEA
E54698
E96AAD
F1A4CE
F9D9EA
FCEFF6

```html
<!DOCTYPE html>
<html lang="en">
<head>
<meta charset="utf-8">
<title>TaalVan – Dine-in Menu</title>
<link rel="stylesheet" href="https://fonts.googleapis.com/css2?family=Montserrat:wght@400;500;700;800&display=swap">
<style>
  :root{
    --canvas:#ffffff;
    --paper:#f2f2f1;
    --paper-grain:#e9e9e8;
    --ink:#2a2a2a;
    --ink-soft:#7a7a7a;
    --lime:#b6d532;
    --lime-deep:#a4c41f;
    --orange:#f7941d;
    --sun:#f5c518;
    --leader:#9a9a9a;
  }
  *{box-sizing:border-box;margin:0;padding:0}
  html,body{width:1200px;height:4000px;overflow:hidden;background:var(--canvas)}
  body{position:relative;font-family:"Montserrat",sans-serif;color:var(--ink)}

  .page{
    position:absolute;left:186px;width:825px;height:1170px;overflow:hidden;
    background:repeating-linear-gradient(90deg,var(--paper) 0 22px,var(--paper-grain) 22px 23px,var(--paper) 23px 61px,#ececeb 61px 62px);
    box-shadow:0 6px 22px rgba(0,0,0,.28);
  }
  .page--one{top:85px}
  .page--two{top:1347px}
  .page--three{top:2621px}

  .menu-box{position:absolute;border:2px dashed var(--orange)}
  .menu-label{
    position:absolute;top:-14px;height:40px;padding:0 30px;
    display:flex;align-items:center;justify-content:center;
    background:var(--lime);border-radius:6px 18px 8px 20px;
    font-weight:800;font-size:16px;letter-spacing:.2px;color:var(--ink);text-transform:uppercase;white-space:nowrap;
    box-shadow:inset 0 -4px 0 var(--lime-deep);
  }
  .items{position:absolute;left:18px;right:18px;list-style:none}
  .item{height:26.7px;display:grid;grid-template-columns:auto 1fr 34px;grid-template-rows:16px 10px;column-gap:6px}
  .item-name{font-size:14px;font-weight:500;line-height:16px;white-space:nowrap}
  .item-leader{border-bottom:1.5px dotted var(--leader);margin-bottom:4px}
  .item-price{font-size:13px;text-align:right;line-height:16px}
  .item-note{grid-column:1 / 4;font-size:7.5px;line-height:9px;color:var(--ink-soft)}

  .photo{position:absolute}
  .brand{position:absolute;left:340px;top:70px;display:flex;align-items:center;gap:10px}
  .brand-dot{width:34px;height:34px;border-radius:50%;background:var(--sun)}
  .brand-name{font-family:"Montserrat",sans-serif;font-weight:800;font-size:30px;color:var(--ink)}
</style>
</head>
<body>

<!-- Page one -->
<article class="page page--one">
  <div class="photo" role="img" aria-label="Masala dosa on a plate with chutney bowls and a yellow paint splash" style="left:0;top:0;width:240px;height:224px;border-radius:0 0 120px 0;background:radial-gradient(circle at 40% 40%,#e7b75c,#d98f2c 55%,#f5c518 80%,transparent 81%)"></div>
  <div class="photo" role="img" aria-label="Idli on a wooden plate with sambar" style="left:635px;top:0;width:190px;height:147px;border-radius:0 0 0 95px;background:radial-gradient(circle at 60% 35%,#f4f1e8,#e6dfcf 45%,#7a4a2a 75%,transparent 76%)"></div>
  <div class="photo" role="img" aria-label="Medu vada with sambar and chutneys on a banana leaf" style="left:472px;top:1006px;width:353px;height:164px;border-radius:120px 0 0 0;background:radial-gradient(circle at 50% 60%,#c47a2c,#8a5a2a 40%,#4f8a2c 70%,#f5c518 90%)"></div>

  <div class="brand"><span class="brand-dot"></span><span class="brand-name">TaalVan</span></div>

  <section class="menu-box" style="left:46px;top:240px;width:369px;height:886px">
    <h2 class="menu-label" style="left:24px">Our Speciality Dosa</h2>
    <ul class="items" style="top:50px">
      <li class="item"><span class="item-name">Plain Dosa</span><span class="item-leader"></span><span class="item-price">14</span><span class="item-note">It is a long established</span></li>
      <li class="item"><span class="item-name">Masala Dosa</span><span class="item-leader"></span><span class="item-price">16</span><span class="item-note">It is a long established</span></li>
      <li class="item"><span class="item-name">Mysore Masala Dosa</span><span class="item-leader"></span><span class="item-price">16</span><span class="item-note">It is a long established</span></li>
      <li class="item"><span class="item-name">Sweet and Spicy Dosa</span><span class="item-leader"></span><span class="item-price">16</span><span class="item-note">It is a long established</span></li>
      <li class="item"><span class="item-name">Sweet and Spicy Masala Dosa</span><span class="item-leader"></span><span class="item-price">17</span><span class="item-note">It is a long established</span></li>
      <li class="item"><span class="item-name">Kara Dosa</span><span class="item-leader"></span><span class="item-price">15</span><span class="item-note">It is a long established</span></li>
      <li class="item"><span class="item-name">Kara Masala Dosa</span><span class="item-leader"></span><span class="item-price">17</span><span class="item-note">It is a long established</span></li>
      <li class="item"><span class="item-name">Ghee Dosa</span><span class="item-leader"></span><span class="item-price">16</span><span class="item-note">It is a long established</span></li>
      <li class="item"><span class="item-name">Ghee Podi Dosa</span><span class="item-leader"></span><span class="item-price">17</span><span class="item-note">It is a long established</span></li>
      <li class="item"><span class="item-name">Ghee Podi Masala Dosa</span><span class="item-leader"></span><span class="item-price">19</span><span class="item-note">It is a long established</span></li>
      <li class="item"><span class="item-name">Paper Ghee Roast Dosa</span><span class="item-leader"></span><span class="item-price">17</span><span class="item-note">It is a long established</span></li>
      <li class="item"><span class="item-name">Paper Ghee Roast Masala Dosa</span><span class="item-leader"></span><span class="item-price">19</span><span class="item-note">It is a long established</span></li>
      <li class="item"><span class="item-name">Paper Dosa</span><span class="item-leader"></span><span class="item-price">16</span><span class="item-note">It is a long established</span></li>
      <li class="item"><span class="item-name">Spring Mix Dosa</span><span class="item-leader"></span><span class="item-price">18</span><span class="item-note">It is a long established</span></li>
      <li class="item"><span class="item-name">Spinach Dosa</span><span class="item-leader"></span><span class="item-price">16</span><span class="item-note">It is a long established</span></li>
      <li class="item"><span class="item-name">Spinach Cheese Dosa</span><span class="item-leader"></span><span class="item-price">18</span><span class="item-note">It is a long established</span></li>
      <li class="item"><span class="item-name">Cheese Dosa</span><span class="item-leader"></span><span class="item-price">16</span><span class="item-note">It is a long established</span></li>
      <li class="item"><span class="item-name">Chilli Cheese Dosa</span><span class="item-leader"></span><span class="item-price">17</span><span class="item-note">It is a long established</span></li>
      <li class="item"><span class="item-name">Cheese Masala Dosa</span><span class="item-leader"></span><span class="item-price">18</span><span class="item-note">It is a long established</span></li>
      <li class="item"><span class="item-name">Mint Dosa</span><span class="item-leader"></span><span class="item-price">16</span><span class="item-note">It is a long established</span></li>
      <li class="item"><span class="item-name">Gongura Dosa</span><span class="item-leader"></span><span class="item-price">17</span><span class="item-note">It is a long established</span></li>
      <li class="item"><span class="item-name">Onion Dosa</span><span class="item-leader"></span><span class="item-price">15</span><span class="item-note">It is a long established</span></li>
      <li class="item"><span class="item-name">Onion Masala Dosa</span><span class="item-leader"></span><span class="item-price">17</span><span class="item-note">It is a long established</span></li>
      <li class="item"><span class="item-name">Onion Chilli Dosa</span><span class="item-leader"></span><span class="item-price">16</span><span class="item-note">It is a long established</span></li>
      <li class="item"><span class="item-name">Onion Chilli Masala Dosa</span><span class="item-leader"></span><span class="item-price">18</span><span class="item-note">It is a long established</span></li>
      <li class="item"><span class="item-name">Paneer Dosa</span><span class="item-leader"></span><span class="item-price">17</span><span class="item-note">It is a long established</span></li>
      <li class="item"><span class="item-name">Paneer Masala Dosa</span><span class="item-leader"></span><span class="item-price">19</span><span class="item-note">It is a long established</span></li>
      <li class="item"><span class="item-name">Pav Bhaji Dosa</span><span class="item-leader"></span><span class="item-price">18</span><span class="item-note">It is a long established</span></li>
      <li class="item"><span class="item-name">TaalVan Grand Dosa</span><span class="item-leader"></span><span class="item-price">40</span><span class="item-note">It is a long established</span></li>
      <li class="item"><span class="item-name">Chicken Keema Dosa</span><span class="item-leader"></span><span class="item-price">20</span><span class="item-note">It is a long established</span></li>
      <li class="item"><span class="item-name">Lamb Keema Dosa</span><span class="item-leader"></span><span class="item-price">21</span><span class="item-note">It is a long established</span></li>
    </ul>
  </section>

  <section class="menu-box" style="left:438px;top:181px;width:338px;height:562px">
    <h2 class="menu-label" style="left:22px">Our Speciality Dosa</h2>
    <ul class="items" style="top:42px">
      <li class="item"><span class="item-name">Rava Dosa</span><span class="item-leader"></span><span class="item-price">18</span><span class="item-note">It is a long established</span></li>
      <li class="item"><span class="item-name">Rava Onion Dosa</span><span class="item-leader"></span><span class="item-price">19</span><span class="item-note">It is a long established</span></li>
      <li class="item"><span class="item-name">Rava Onion Chilli Dosa</span><span class="item-leader"></span><span class="item-price">20</span><span class="item-note">It is a long established</span></li>
      <li class="item"><span class="item-name">Rava Masala Dosa</span><span class="item-leader"></span><span class="item-price">20</span><span class="item-note">It is a long established</span></li>
      <li class="item"><span class="item-name">Rava Ghee Dosa</span><span class="item-leader"></span><span class="item-price">20</span><span class="item-note">It is a long established</span></li>
      <li class="item"><span class="item-name">Rava Ghee Masala Dosa</span><span class="item-leader"></span><span class="item-price">21</span><span class="item-note">It is a long established</span></li>
      <li class="item"><span class="item-name">Cone Dosa</span><span class="item-leader"></span><span class="item-price">11</span><span class="item-note">It is a long established</span></li>
      <li class="item"><span class="item-name">Hazelnut/Chocolate Dosa</span><span class="item-leader"></span><span class="item-price">13</span><span class="item-note">It is a long established</span></li>
      <li class="item"><span class="item-name">Plain Uthappam</span><span class="item-leader"></span><span class="item-price">12</span><span class="item-note">It is a long established</span></li>
      <li class="item"><span class="item-name">Onion Chilli Uthappam</span><span class="item-leader"></span><span class="item-price">14</span><span class="item-note">It is a long established</span></li>
      <li class="item"><span class="item-name">Cheese Chilli Uthappam</span><span class="item-leader"></span><span class="item-price">15</span><span class="item-note">It is a long established</span></li>
      <li class="item"><span class="item-name">Cheese Uthappam</span><span class="item-leader"></span><span class="item-price">14</span><span class="item-note">It is a long established</span></li>
      <li class="item"><span class="item-name">Chilli Uthappam</span><span class="item-leader"></span><span class="item-price">13</span><span class="item-note">It is a long established</span></li>
      <li class="item"><span class="item-name">Chilli Onion Uthappam</span><span class="item-leader"></span><span class="item-price">14</span><span class="item-note">It is a long established</span></li>
      <li class="item"><span class="item-name">Mix Veg Uthappam</span><span class="item-leader"></span><span class="item-price">15</span><span class="item-note">It is a long established</span></li>
      <li class="item"><span class="item-name">Mix Veg Chilli Uthappam</span><span class="item-leader"></span><span class="item-price">16</span><span class="item-note">It is a long established</span></li>
      <li class="item"><span class="item-name">Mix Veg Tomato Uthappam</span><span class="item-leader"></span><span class="item-price">16</span><span class="item-note">It is a long established</span></li>
      <li class="item"><span class="item-name">Tomato Onion Uthappam</span><span class="item-leader"></span><span class="item-price">16</span><span class="item-note">It is a long established</span></li>
      <li class="item"><span class="item-name">Tomato Onion Chilli Uthappam</span><span class="item-leader"></span><span class="item-price">14</span><span class="item-note">It is a long established</span></li>
    </ul>
  </section>

  <section class="menu-box" style="left:438px;top:769px;width:338px;height:245px">
    <h2 class="menu-label" style="left:22px">Our Speciality Idly</h2>
    <ul class="items" style="top:46px">
      <li class="item"><span class="item-name">Idly</span><span class="item-leader"></span><span class="item-price">12</span><span class="item-note">It is a long established</span></li>
      <li class="item"><span class="item-name">Masala Idly</span><span class="item-leader"></span><span class="item-price">13</span><span class="item-note">It is a long established</span></li>
      <li class="item"><span class="item-name">Podi Idly</span><span class="item-leader"></span><span class="item-price">13</span><span class="item-note">It is a long established</span></li>
      <li class="item"><span class="item-name">Ghee Podi Idly</span><span class="item-leader"></span><span class="item-price">14</span><span class="item-note">It is a long established</span></li>
      <li class="item"><span class="item-name">Bell pepper Idly</span><span class="item-leader"></span><span class="item-price">13</span><span class="item-note">It is a long established</span></li>
      <li class="item"><span class="item-name">Chilli Idly</span><span class="item-leader"></span><span class="item-price">13</span><span class="item-note">It is a long established</span></li>
      <li class="item"><span class="item-name">Rasam Idly</span><span class="item-leader"></span><span class="item-price">15</span><span class="item-note">It is a long established</span></li>
    </ul>
  </section>
</article>

<!-- Page two -->
<article class="page page--two">
  <section class="menu-box" style="left:46px;top:62px;width:369px;height:190px">
    <h2 class="menu-label" style="left:24px">Our Speciality Vada</h2>
    <ul class="items" style="top:44px">
      <li class="item"><span class="item-name">Vada</span><span class="item-leader"></span><span class="item-price">12</span><span class="item-note">It is a long established</span></li>
      <li class="item"><span class="item-name">Rasam Vada</span><span class="item-leader"></span><span class="item-price">15</span><span class="item-note">It is a long established</span></li>
      <li class="item"><span class="item-name">Sambar Vada</span><span class="item-leader"></span><span class="item-price">15</span><span class="item-note">It is a long established</span></li>
      <li class="item"><span class="item-name">Sweet Dahi Vada</span><span class="item-leader"></span><span class="item-price">15</span><span class="item-note">It is a long established</span></li>
      <li class="item"><span class="item-name">Salt Dahi Vada</span><span class="item-leader"></span><span class="item-price">15</span><span class="item-note">It is a long established</span></li>
    </ul>
  </section>

  <section class="menu-box" style="left:46px;top:282px;width:369px;height:136px">
    <h2 class="menu-label" style="left:24px">Our Speciality Puri</h2>
    <ul class="items" style="top:46px">
      <li class="item"><span class="item-name">Puri Chana</span><span class="item-leader"></span><span class="item-price">15</span><span class="item-note">It is a long established</span></li>
      <li class="item"><span class="item-name">Puri Masala</span><span class="item-leader"></span><span class="item-price">15</span><span class="item-note">It is a long established</span></li>
      <li class="item"><span class="item-name">Chole Bhatura</span><span class="item-leader"></span><span class="item-price">18</span><span class="item-note">It is a long established</span></li>
    </ul>
  </section>

  <section class="menu-box" style="left:46px;top:444px;width:369px;height:192px">
    <h2 class="menu-label" style="left:24px;width:184px">Soups</h2>
    <ul class="items" style="top:50px">
      <li class="item"><span class="item-name">Tomato Dhaniya Shorba</span><span class="item-leader"></span><span class="item-price">8</span><span class="item-note">It is a long established</span></li>
      <li class="item"><span class="item-name">Coconut Mushroom</span><span class="item-leader"></span><span class="item-price">8</span><span class="item-note">It is a long established</span></li>
      <li class="item"><span class="item-name">Coconut Chicken</span><span class="item-leader"></span><span class="item-price">9</span><span class="item-note">It is a long established</span></li>
      <li class="item"><span class="item-name">Manchow Veg</span><span class="item-leader"></span><span class="item-price">8</span><span class="item-note">It is a long established</span></li>
      <li class="item"><span class="item-name">Manchow Chicken</span><span class="item-leader"></span><span class="item-price">9</span><span class="item-note">It is a long established</span></li>
    </ul>
  </section>

  <section class="menu-box" style="left:46px;top:663px;width:369px;height:220px">
    <h2 class="menu-label" style="left:24px;width:184px">Drinks</h2>
    <ul class="items" style="top:50px">
      <li class="item"><span class="item-name">Mango Mirchi Drink</span><span class="item-leader"></span><span class="item-price">7</span><span class="item-note">It is a long established</span></li>
      <li class="item"><span class="item-name">Mojito Drink</span><span class="item-leader"></span><span class="item-price">7</span><span class="item-note">It is a long established</span></li>
      <li class="item"><span class="item-name">Indian Tea</span><span class="item-leader"></span><span class="item-price">5</span><span class="item-note">It is a long established</span></li>
      <li class="item"><span class="item-name">Madras Coffee</span><span class="item-leader"></span><span class="item-price">5</span><span class="item-note">It is a long established</span></li>
      <li class="item"><span class="item-name">Black Tea</span><span class="item-leader"></span><span class="item-price">5</span><span class="item-note">It is a long established</span></li>
      <li class="item"><span class="item-name">Indian Espresso - Strong</span><span class="item-leader"></span><span class="item-price">5</span><span class="item-note">It is a long established</span></li>
    </ul>
  </section>

  <section class="menu-box" style="left:46px;top:908px;width:369px;height:246px">
    <h2 class="menu-label" style="left:24px;width:184px">Chaat</h2>
    <ul class="items" style="top:46px">
      <li class="item"><span class="item-name">Pani Puri</span><span class="item-leader"></span><span class="item-price">12</span><span class="item-note">It is a long established</span></li>
      <li class="item"><span class="item-name">Papdi Chat</span><span class="item-leader"></span><span class="item-price">15</span><span class="item-note">It is a long established</span></li>
      <li class="item"><span class="item-name">Tikki Chaat</span><span class="item-leader"></span><span class="item-price">15</span><span class="item-note">It is a long established</span></li>
      <li class="item"><span class="item-name">Samosa Chaat</span><span class="item-leader"></span><span class="item-price">15</span><span class="item-note">It is a long established</span></li>
      <li class="item"><span class="item-name">Pav Bhaji</span><span class="item-leader"></span><span class="item-price">18</span><span class="item-note">It is a long established</span></li>
      <li class="item"><span class="item-name">Mumbai Vada Pav</span><span class="item-leader"></span><span class="item-price">18</span><span class="item-note">It is a long established</span></li>
      <li class="item"><span class="item-name">Anaari Dahi Balla</span><span class="item-leader"></span><span class="item-price">18</span><span class="item-note">It is a long established</span></li>
    </ul>
  </section>

  <section class="menu-box" style="left:433px;top:62px;width:343px;height:222px">
    <h2 class="menu-label" style="left:26px;width:184px">Lite Snacks</h2>
    <ul class="items" style="top:50px">
      <li class="item"><span class="item-name">Aloo Samosa</span><span class="item-leader"></span><span class="item-price">9</span><span class="item-note">It is a long established</span></li>
      <li class="item"><span class="item-name">Onion Pakora</span><span class="item-leader"></span><span class="item-price">12</span><span class="item-note">It is a long established</span></li>
      <li class="item"><span class="item-name">Aloo Tikki</span><span class="item-leader"></span><span class="item-price">9</span><span class="item-note">It is a long established</span></li>
      <li class="item"><span class="item-name">Goat Chukka</span><span class="item-leader"></span><span class="item-price">22</span><span class="item-note">It is a long established</span></li>
      <li class="item"><span class="item-name">Chicken Chukka</span><span class="item-leader"></span><span class="item-price">20</span><span class="item-note">It is a long established</span></li>
      <li class="item"><span class="item-name">Pepper Chicken</span><span class="item-leader"></span><span class="item-price">19</span><span class="item-note">It is a long established</span></li>
    </ul>
  </section>

  <section class="menu-box" style="left:433px;top:319px;width:343px;height:142px">
    <h2 class="menu-label" style="left:26px;width:230px">Special Biryani</h2>
    <ul class="items" style="top:52px">
      <li class="item"><span class="item-name">Boneless Chicken Biryani</span><span class="item-leader"></span><span class="item-price">20</span><span class="item-note">It is a long established</span></li>
      <li class="item"><span class="item-name">Prawns Biryani</span><span class="item-leader"></span><span class="item-price">21</span><span class="item-note">It is a long established</span></li>
      <li class="item"><span class="item-name">Kheema Biryani</span><span class="item-leader"></span><span class="item-price">21</span><span class="item-note">It is a long established</span></li>
    </ul>
  </section>

  <div class="photo" role="img" aria-label="Chicken biryani in a copper bowl with fried onions and whole spices" style="left:441px;top:488px;width:441px;height:441px;border-radius:50%;background:radial-gradient(circle at 45% 40%,#e9c37a,#d9a24b 40%,#b9742e 65%,#6b3f1e 72%,transparent 73%)"></div>
  <div class="photo" role="img" aria-label="Pani puri topped with chickpeas and chutney on a plate" style="left:441px;top:944px;width:384px;height:226px;border-radius:160px 0 0 0;background:radial-gradient(circle at 55% 55%,#e8b45f,#d89a3d 45%,#c9c4bb 75%,transparent 76%)"></div>
</article>

<!-- Page three -->
<article class="page page--three">
  <section class="menu-box" style="left:50px;top:65px;width:346px;height:328px">
    <h2 class="menu-label" style="left:28px;width:224px">Appetizers</h2>
    <ul class="items" style="top:50px">
      <li class="item"><span class="item-name">Choose your protein</span><span class="item-leader"></span><span class="item-price">17</span><span class="item-note">It is a long established</span></li>
      <li class="item"><span class="item-name">Cauliflower</span><span class="item-leader"></span><span class="item-price">19</span><span class="item-note">It is a long established</span></li>
      <li class="item"><span class="item-name">Baby Corn</span><span class="item-leader"></span><span class="item-price">19</span><span class="item-note">It is a long established</span></li>
      <li class="item"><span class="item-name">Paneer</span><span class="item-leader"></span><span class="item-price">20</span><span class="item-note">It is a long established</span></li>
      <li class="item"><span class="item-name">Chicken</span><span class="item-leader"></span><span class="item-price">21</span><span class="item-note">It is a long established</span></li>
      <li class="item"><span class="item-name">Fish</span><span class="item-leader"></span><span class="item-price">23</span><span class="item-note">It is a long established</span></li>
      <li class="item"><span class="item-name">King Prawn/Shrimp</span><span class="item-leader"></span><span class="item-price">23</span><span class="item-note">It is a long established</span></li>
      <li class="item"><span class="item-name">And Pick your Flavour</span><span class="item-leader"></span><span class="item-price">23</span><span class="item-note">It is a long established</span></li>
      <li class="item"><span class="item-name">Schezwan</span><span class="item-leader"></span><span class="item-price">23</span><span class="item-note">It is a long established</span></li>
      <li class="item"><span class="item-name">Honey Garlic</span><span class="item-leader"></span><span class="item-price">23</span><span class="item-note">It is a long established</span></li>
    </ul>
  </section>

  <section class="menu-box" style="left:438px;top:65px;width:338px;height:328px">
    <h2 class="menu-label" style="left:26px;width:224px">Hakka</h2>
    <ul class="items" style="top:50px">
      <li class="item"><span class="item-name">Hakka Noodles or Fried Rice</span><span class="item-leader"></span><span class="item-price">18</span><span class="item-note">It is a long established</span></li>
      <li class="item"><span class="item-name">Choose your protein</span><span class="item-leader"></span><span class="item-price">12</span><span class="item-note">It is a long established</span></li>
      <li class="item"><span class="item-name">Egg</span><span class="item-leader"></span><span class="item-price">13</span><span class="item-note">It is a long established</span></li>
      <li class="item"><span class="item-name">Chicken</span><span class="item-leader"></span><span class="item-price">14</span><span class="item-note">It is a long established</span></li>
      <li class="item"><span class="item-name">Shrimp</span><span class="item-leader"></span><span class="item-price">14</span><span class="item-note">It is a long established</span></li>
      <li class="item"><span class="item-name">Schezwan Noodles or Fried Rice</span><span class="item-leader"></span><span class="item-price">18</span><span class="item-note">It is a long established</span></li>
      <li class="item"><span class="item-name">Choose your protein</span><span class="item-leader"></span><span class="item-price">12</span><span class="item-note">It is a long established</span></li>
      <li class="item"><span class="item-name">Egg</span><span class="item-leader"></span><span class="item-price">12</span><span class="item-note">It is a long established</span></li>
      <li class="item"><span class="item-name">Chicken</span><span class="item-leader"></span><span class="item-price">13</span><span class="item-note">It is a long established</span></li>
      <li class="item"><span class="item-name">Shrimp</span><span class="item-leader"></span><span class="item-price">14</span><span class="item-note">It is a long established</span></li>
    </ul>
  </section>

  <section class="menu-box" style="left:50px;top:426px;width:346px;height:300px">
    <h2 class="menu-label" style="left:28px;width:224px">Veg Curries</h2>
    <ul class="items" style="top:50px">
      <li class="item"><span class="item-name">Paneer Tikka Masala</span><span class="item-leader"></span><span class="item-price">19</span><span class="item-note">It is a long established</span></li>
      <li class="item"><span class="item-name">Paneer Methi Garlic</span><span class="item-leader"></span><span class="item-price">19</span><span class="item-note">It is a long established</span></li>
      <li class="item"><span class="item-name">Veg Jaipuri</span><span class="item-leader"></span><span class="item-price">19</span><span class="item-note">It is a long established</span></li>
      <li class="item"><span class="item-name">Diwani Handi</span><span class="item-leader"></span><span class="item-price">19</span><span class="item-note">It is a long established</span></li>
      <li class="item"><span class="item-name">Paneer Bhurji</span><span class="item-leader"></span><span class="item-price">19</span><span class="item-note">It is a long established</span></li>
      <li class="item"><span class="item-name">Creamy Corn Methi</span><span class="item-leader"></span><span class="item-price">19</span><span class="item-note">It is a long established</span></li>
      <li class="item"><span class="item-name">Paneer Capsicum</span><span class="item-leader"></span><span class="item-price">19</span><span class="item-note">It is a long established</span></li>
      <li class="item"><span class="item-name">Dal Bhukara</span><span class="item-leader"></span><span class="item-price">19</span><span class="item-note">It is a long established</span></li>
      <li class="item"><span class="item-name">Dal fry</span><span class="item-leader"></span><span class="item-price">19</span><span class="item-note">It is a long established</span></li>
    </ul>
  </section>

  <section class="menu-box" style="left:438px;top:426px;width:338px;height:380px">
    <h2 class="menu-label" style="left:26px;width:224px">Non-Veg Curries</h2>
    <ul class="items" style="top:50px">
      <li class="item"><span class="item-name">South Indian Chicken Curry</span><span class="item-leader"></span><span class="item-price">21</span><span class="item-note">It is a long established</span></li>
      <li class="item"><span class="item-name">Butter Chicken</span><span class="item-leader"></span><span class="item-price">21</span><span class="item-note">It is a long established</span></li>
      <li class="item"><span class="item-name">Chicken Tikka Masala</span><span class="item-leader"></span><span class="item-price">21</span><span class="item-note">It is a long established</span></li>
      <li class="item"><span class="item-name">Spinach Chicken</span><span class="item-leader"></span><span class="item-price">21</span><span class="item-note">It is a long established</span></li>
      <li class="item"><span class="item-name">Kadai Chicken</span><span class="item-leader"></span><span class="item-price">21</span><span class="item-note">It is a long established</span></li>
      <li class="item"><span class="item-name">Goat Curry</span><span class="item-leader"></span><span class="item-price">23</span><span class="item-note">It is a long established</span></li>
      <li class="item"><span class="item-name">Goat Vindaloo</span><span class="item-leader"></span><span class="item-price">23</span><span class="item-note">It is a long established</span></li>
      <li class="item"><span class="item-name">Goat Korma</span><span class="item-leader"></span><span class="item-price">23</span><span class="item-note">It is a long established</span></li>
      <li class="item"><span class="item-name">Spicy Goat Curry</span><span class="item-leader"></span><span class="item-price">23</span><span class="item-note">It is a long established</span></li>
      <li class="item"><span class="item-name">Kadai Goat</span><span class="item-leader"></span><span class="item-price">23</span><span class="item-note">It is a long established</span></li>
      <li class="item"><span class="item-name">Malabai Fish</span><span class="item-leader"></span><span class="item-price">23</span><span class="item-note">It is a long established</span></li>
      <li class="item"><span class="item-name">Malabar Shrimp</span><span class="item-leader"></span><span class="item-price">23</span><span class="item-note">It is a long established</span></li>
    </ul>
  </section>

  <div class="photo" role="img" aria-label="Spread of tandoori chicken, hakka noodles, puri with green chutney and a bowl of curry" style="left:0;top:824px;width:825px;height:346px;background:linear-gradient(90deg,#a8472a 0%,#d98a3c 22%,#e9c27a 40%,#3f4a55 55%,#d4722a 75%,#e58a2e 100%);clip-path:ellipse(80% 100% at 50% 100%)"></div>
</article>

</body>
</html>
```